'The Paperlanterns' - Album Artwork Needed!!

Looking for album artwork design for a new pop/rock original band from NJ called 'The Paperlanterns'. The debut EP is entitled 'Hold the Door'.

The group is a 4 piece with a lead singer/guitar player, bass player, guitar player, and drummer. There are also piano parts on the songs played by the singer. Stylistically similar to a Bright Harbor Kids/Folds the Map/Vesper kind of vibe.

We need designs for both the front and rear of the CD sleeve as well as printing on the CD itself. We're leaning towards photo based artwork that captures the intensity of our music but we are not opposed to graphic design.

If there were a mission statement and an idea we would want to convey for the band it would be fun, energetic, happy, feel good, pumped up, moving, dynamic, get people going, powerful, lively rock songs with catchy hooks.

Energy! Energy! Energy!

Give me your best work! Lets get vibrant fun and memorable.

Let me know if you have questions!

Reason: Definitely some good designs. Going to extend it for 5 days in case there are any extras. Still open....

Reason: Still trying to narrow down the right paperlanterns EP cover. Some great designs so far. We need to pick one within the next 7 days so nows the last chance. Think colorful and fun! Let me know if you h ave any questions

Hi Designers, Seen some great work! We need to send the CD off to get manufactured so we need to pick our design ASAP! We've changed this to a committed payment project. We also increased the payment amount and listed this as a featured project. Bring your best work and please view the brief first. Any questions be sure to ask!

Reason: We've increased the payment and upgraded this to a committed project. We want to see what you've got! This is our absolute deadline as the CD needs to get manufactured ASAP! Thanks!

A lot of good ideas, not sure we found the one that captures the vibe we're going for, but we definitely need to pick ASAP! Message us if you have questions! Theo

Reason: More Designs!

Designer's - great work is coming in. Please use the font: JennaSue.ttf for the band's name 'The Paperlanterns'. The rest is all open to interpretation. Remember colorful fun and energetic!

...Also we've decided to remove the last two bonus tracks so the EP is only going to be the 5 songs: 1.) The Undertow 2.) Edge of the Porch 3.) Marnie 4.) Drifters 5.) Running Late Always Felt So Right

Designers! I have uploaded a file that contains the template for the artwork. The design will need to fit these template. Theres one for the outside of the CD and another for the face of the CD. Please let me know if you have any questions! Thank you, Theo

Target Market(s)

Younger audience 16-30

Industry/Entity Type

Printing

Requirements
Must have
• Vibrant in either color or photography
Should not have
• Photos of the band members as the design.

I provided from photos so you can get an idea for the band, but I do NOT want those used as the album artwork.

Please do not use these pictures on your design!
Thanks!

```html
<!DOCTYPE html>
<html lang="en">
<head>
<meta charset="utf-8">
<title>The Paperlanterns — Hold the Door</title>
<link rel="stylesheet" href="https://fonts.googleapis.com/css2?family=Jost:wght@400;500&display=swap">
<style>
  :root {
    --paper: #ffffff;
    --ink: #000000;
    --title: #ffffff;
    --tile-edge: rgba(120, 150, 130, 0.35);
  }
  html, body {
    margin: 0;
    padding: 0;
    overflow: hidden;
    background: var(--paper);
  }
  .cover {
    width: 1200px;
    height: 1200px;
    box-sizing: border-box;
    padding: 14.4px;
    display: grid;
    grid-template-columns: repeat(5, 1fr);
    grid-template-rows: repeat(5, 1fr);
    gap: 14.4px;
    background: var(--paper);
  }
  .tile {
    box-shadow: 0 0 0 1px var(--tile-edge), 0 1px 3px rgba(0, 0, 0, 0.18);
  }
  .title-panel {
    grid-column: 3 / span 3;
    grid-row: 3;
    background: var(--ink);
    display: flex;
    flex-direction: column;
    justify-content: center;
    align-items: center;
    gap: 14px;
    box-shadow: 0 1px 3px rgba(0, 0, 0, 0.25);
  }
  .title-panel .band,
  .title-panel .record {
    margin: 0;
    color: var(--title);
    font-family: "Jost", "Futura", sans-serif;
    font-weight: 500;
    text-transform: uppercase;
    letter-spacing: 0.11em;
    line-height: 1;
    white-space: nowrap;
  }
  .title-panel .band { font-size: 46px; }
  .title-panel .record { font-size: 56px; }

  .t-walker   { background: linear-gradient(135deg, #6d6f6b, #c9a94a 55%, #8a2a24); }
  .t-slides   { background: linear-gradient(135deg, #d7d9db, #8c9096 60%, #3a3c40); }
  .t-sign     { background: linear-gradient(135deg, #eeeeee, #c4c4c4 50%, #9b9a86); }
  .t-bokeh    { background: radial-gradient(circle at 60% 35%, #3fe0e6, #1b6d78 45%, #0d2530); }
  .t-crossing { background: linear-gradient(160deg, #2b1b10, #8a4a24 55%, #c9372a); }
  .t-neon-a   { background: linear-gradient(135deg, #ff9b1f, #e63a12 50%, #ffd35a); }
  .t-bulbs    { background: radial-gradient(circle at 50% 50%, #6a5030, #fff2c4 30%, #8e6a3c 70%, #3b2a18); }
  .t-pattern  { background: linear-gradient(135deg, #1c1c1c, #8c8c8c 50%, #2a2a2a); }
  .t-neon-b   { background: linear-gradient(90deg, #ff3d1a, #ff6a9c 40%, #2ec9f0 70%, #f23a24); }
  .t-stage    { background: radial-gradient(circle at 55% 25%, #f2f2f2, #8a8e96 45%, #1a1c20); }
  .t-cat      { background: radial-gradient(circle at 45% 50%, #8a5a1e, #d6b062 45%, #f6ecb0); }
  .t-balloons { background: linear-gradient(135deg, #1e6df0, #ff3a6c 35%, #2ed0f0 65%, #f0e03a); }
  .t-window   { background: linear-gradient(160deg, #3a2a24, #b0312a 40%, #4a6a80 75%, #c8c8c8); }
  .t-chalk    { background: linear-gradient(135deg, #3a3c40, #2a2c30 60%, #4a4e50); }
  .t-static   { background: repeating-linear-gradient(90deg, #9a9c9e 0 2px, #d6d8da 2px 5px, #7a7c7e 5px 6px); }
  .t-doll     { background: radial-gradient(circle at 50% 55%, #e8a0b0, #7a5a5a 45%, #1c1c1c 75%); }
  .t-type     { background: linear-gradient(135deg, #2a2a2a, #a8a8a8 50%, #3c3c3c); }
  .t-rocks    { background: linear-gradient(150deg, #b8a070, #6e5a3a 50%, #d6d0c4); }
  .t-walkers  { background: linear-gradient(180deg, #d4d2cc, #8e8e70 50%, #c8c6c0); }
  .t-letters  { background: radial-gradient(circle at 30% 30%, #f4f4f0, #7a6a50 45%, #1e1a14); }
  .t-neon-c   { background: linear-gradient(135deg, #6a1ca0, #ff3ad0 45%, #2a9cf0); }
  .t-eye      { background: radial-gradient(circle at 50% 50%, #3a1010, #e02a1e 35%, #6a8ab0 70%, #e8e4dc); }
</style>
</head>
<body>
  <main class="cover">
    <div class="tile t-walker" role="img" aria-label="Photo of a man in a yellow shirt walking past a red bus"></div>
    <div class="tile t-slides" role="img" aria-label="Photo of a pile of mounted film slides"></div>
    <div class="tile t-sign" role="img" aria-label="Photo of a small warning sign on a patterned surface"></div>
    <div class="tile t-bokeh" role="img" aria-label="Photo of blurred teal city lights through a wet windshield"></div>
    <div class="tile t-crossing" role="img" aria-label="Night photo of a railroad crossing with red signal lights"></div>

    <div class="tile t-neon-a" role="img" aria-label="Photo of glowing orange and red neon tubes"></div>
    <div class="tile t-bulbs" role="img" aria-label="Photo of a mirror framed by round light bulbs"></div>
    <div class="tile t-pattern" role="img" aria-label="Photo of a woman in a floral dress against a black and white mural"></div>
    <div class="tile t-neon-b" role="img" aria-label="Photo of blurred red, pink and blue neon lights"></div>
    <div class="tile t-stage" role="img" aria-label="Photo of silhouetted figures against a bright projection screen"></div>

    <div class="tile t-cat" role="img" aria-label="Warm soft-focus photo of a tabby cat"></div>
    <div class="tile t-balloons" role="img" aria-label="Photo of a heap of colourful uninflated balloons"></div>
    <section class="title-panel">
      <h1 class="band">The Paperlanterns</h1>
      <h2 class="record">Hold the Door</h2>
    </section>

    <div class="tile t-window" role="img" aria-label="Photo of a shop window with neon signs and street reflections"></div>
    <div class="tile t-chalk" role="img" aria-label="Photo of chalk doodles and scribbles on a blackboard"></div>
    <div class="tile t-static" role="img" aria-label="Photo of grey television static lines"></div>
    <div class="tile t-doll" role="img" aria-label="Photo of a vintage pink doll on a dark backdrop"></div>
    <div class="tile t-type" role="img" aria-label="Photo of a jumble of metal printing type"></div>

    <div class="tile t-rocks" role="img" aria-label="Vintage photo of a woman seated on rocks beside a rabbit silhouette"></div>
    <div class="tile t-walkers" role="img" aria-label="Photo of two people walking down a pavement"></div>
    <div class="tile t-letters" role="img" aria-label="Photo of blurred mirrored lettering with bokeh lights"></div>
    <div class="tile t-neon-c" role="img" aria-label="Photo of a pink and purple neon sign"></div>
    <div class="tile t-eye" role="img" aria-label="Photo of a red neon ring over an overlaid eye and building"></div>
  </main>
</body>
</html>
```